Exciting & Elegant Stationary Pack

Stationary consists of
1. Letter head / Envelope
2. Business Card
3. Invoice
4. 40x40mm sticker

Attached files;

1. Logo (Other formats available on request)
2. MS word Doc - For information and description of design
3. Website image (This will be our new website so use the colours so everything ties together)
4. Sample of stationary pack we like, but feel free to be creative

Target Market(s)

Home improvement

Industry/Entity Type

Construction

Font styles to use
Other font styles liked:
• Leave up to designer - We like font used on (website attached image)

Requirements
Must have
• Please look at uploaded file of sample website and use colours
Nice to have
• Any type of business card design - eg. metal, die cut, embossed, etc...

```html
<!DOCTYPE html>
<html lang="en">
<head>
<meta charset="utf-8">
<title>Grout &amp; Grain – Business Card</title>
<link rel="stylesheet" href="https://fonts.googleapis.com/css2?family=Arimo:wght@400;700&display=swap">
<style>
  :root {
    --navy: #1f4d72;
    --navy-deep: #173d5c;
    --orange: #f08a3c;
    --orange-deep: #d9782f;
    --paper: #ffffff;
    --paper-shade: #eef0f2;
    --ink: #3a3d42;
    --ink-soft: #7a7e84;
    --rule: #b9bcc0;
    --backdrop: #2c2e31;
  }
  * { box-sizing: border-box; margin: 0; padding: 0; }
  html, body {
    width: 1200px;
    height: 950px;
    overflow: hidden;
    background: var(--backdrop);
    font-family: "Arimo", Arial, sans-serif;
  }
  .sheet {
    width: 1200px;
    height: 950px;
    display: flex;
    flex-direction: column;
    align-items: center;
    justify-content: center;
    gap: 56px;
  }
  .card {
    position: relative;
    width: 640px;
    height: 390px;
    border-radius: 3px;
    overflow: hidden;
    box-shadow: 0 10px 28px rgba(0,0,0,.45);
  }

  /* Back of card */
  .card--back {
    background: linear-gradient(115deg, var(--orange) 0%, var(--orange-deep) 100%);
  }
  .card--back .brand {
    position: absolute;
    left: 50%;
    top: 150px;
    transform: translateX(-50%);
  }
  .card--back .brand__name { color: var(--paper); }
  .card--back .brand__square { background: var(--navy); }
  .card--back .back-url {
    position: absolute;
    left: 0; right: 0;
    top: 250px;
    text-align: center;
    color: rgba(255,255,255,.85);
    font-size: 17px;
    letter-spacing: 4px;
  }

  /* Brand name */
  .brand {
    display: flex;
    align-items: center;
    gap: 12px;
    white-space: nowrap;
  }
  .brand__square {
    width: 26px;
    height: 26px;
    background: var(--orange);
  }
  .brand__name {
    font-weight: 700;
    font-size: 32px;
    letter-spacing: 1px;
    color: var(--navy);
  }

  /* Front of card */
  .card--front {
    background: linear-gradient(160deg, var(--paper) 0%, var(--paper) 55%, var(--paper-shade) 100%);
  }
  .card--front .brand {
    position: absolute;
    right: 44px;
    top: 78px;
  }
  .holder {
    position: absolute;
    left: 44px;
    top: 104px;
  }
  .holder__name {
    font-weight: 700;
    font-size: 24px;
    color: var(--navy);
  }
  .holder__role {
    margin-top: 4px;
    font-size: 17px;
    color: var(--orange);
  }
  .divider {
    position: absolute;
    left: 44px;
    right: 36px;
    top: 178px;
    height: 1px;
    background: var(--rule);
  }
  .contacts {
    position: absolute;
    left: 44px;
    top: 192px;
    list-style: none;
  }
  .contacts li {
    display: flex;
    align-items: center;
    gap: 12px;
    height: 24px;
    font-size: 16px;
    color: var(--ink);
  }
  .contacts svg {
    width: 16px;
    height: 16px;
    fill: var(--navy);
    flex: none;
  }
  .licence {
    position: absolute;
    right: 40px;
    bottom: 62px;
    font-size: 16px;
    color: var(--ink-soft);
  }
  .edge {
    position: absolute;
    left: 0; right: 0;
    bottom: 0;
    height: 20px;
    background: var(--navy-deep);
    border-top: 3px solid var(--orange);
  }
</style>
</head>
<body>
<main class="sheet">

  <section class="card card--front" aria-label="Business card front">
    <div class="brand">
      <span class="brand__square"></span>
      <span class="brand__name">GROUT &amp; GRAIN</span>
    </div>

    <div class="holder">
      <p class="holder__name">Lena Hartley</p>
      <p class="holder__role">Project Manager</p>
    </div>

    <div class="divider"></div>

    <ul class="contacts">
      <li>
        <svg viewBox="0 0 16 16" aria-hidden="true"><path d="M4 0h8a1.5 1.5 0 0 1 1.5 1.5v13A1.5 1.5 0 0 1 12 16H4a1.5 1.5 0 0 1-1.5-1.5v-13A1.5 1.5 0 0 1 4 0zm0 2v10.5h8V2zm4 11.3a.9.9 0 1 0 0 1.8.9.9 0 0 0 0-1.8z"/></svg>
        0400 555 019
      </li>
      <li>
        <svg viewBox="0 0 16 16" aria-hidden="true"><path d="M0 3h16v10H0zm1.6 1.2L8 8.7l6.4-4.5z"/></svg>
        info@groutandgrain.com.au
      </li>
      <li>
        <svg viewBox="0 0 16 16" aria-hidden="true"><path d="M8 0a8 8 0 1 0 0 16A8 8 0 0 0 8 0zm0 1.6a6.4 6.4 0 0 1 5 10.4L9.5 9.6 10 7 7 5 5 6 3.2 4A6.4 6.4 0 0 1 8 1.6z"/></svg>
        www.groutandgrain.com.au
      </li>
    </ul>

    <p class="licence">Lic No.,204518c</p>
    <div class="edge"></div>
  </section>

  <section class="card card--back" aria-label="Business card back">
    <div class="brand">
      <span class="brand__square"></span>
      <span class="brand__name">GROUT &amp; GRAIN</span>
    </div>
    <p class="back-url">groutandgrain.com.au</p>
  </section>

</main>
</body>
</html>
```